Building Custom Homes

We need a new business card design for a new company called " T & R Custom Homes" . We built custom homes according to our client's dream home. We would like to see designs that use the color blue, green, yellow, orange, pink depicting a home happy 'n bright!

Industry/Entity Type

Business

Contact Information for Business Card

Email: porvina73@quellmail.com.au Mobile: 0438 712 946 Phone: 02 6619 3874 Address: Shop 3 / 17 Wendover Lane Coffs Harbour, NSW 2450 Builders License Number : 47 18 3K ABN : 53 917 648 204 Name: Owen Padick

Colors
0355a3
0392cd
9bcb3c
e34297
f78f20
fbed22

Requirements
Must have
• The Company Name : "T & R Custom Homes"
• must depict the building industry

```html
<!DOCTYPE html>
<html lang="en">
<head>
<meta charset="utf-8">
<title>T &amp; R Custom Homes – Business Card</title>
<link href="https://fonts.googleapis.com/css2?family=Jost:wght@400;500;600&display=swap" rel="stylesheet">
<style>
  :root {
    --backdrop: #2b2b2d;
    --frame-orange: #f59a1c;
    --frame-orange-deep: #e8860f;
    --paper: #f4f4f4;
    --paper-shade: #e6e6e6;
    --green: #8cc63e;
    --green-deep: #74ad2c;
    --blue: #0355a3;
    --blue-light: #0392cd;
    --orange-text: #f78f20;
    --white: #ffffff;
  }
  * { box-sizing: border-box; margin: 0; padding: 0; }
  html, body {
    width: 1200px; height: 900px; overflow: hidden;
    background: var(--backdrop);
    font-family: "Jost", "Futura", sans-serif;
  }
  .business-card {
    position: absolute; left: 110px; top: 175px;
    width: 980px; height: 550px;
    background: linear-gradient(135deg, var(--frame-orange), var(--frame-orange-deep));
    padding: 20px;
  }
  .card-face {
    position: relative; width: 100%; height: 100%; overflow: hidden;
    background: linear-gradient(180deg, var(--paper), var(--paper-shade));
  }
  .green-field { position: absolute; inset: 0; width: 100%; height: 100%; }
  .identity {
    position: absolute; left: 250px; top: 62px; text-align: right;
  }
  .person-name {
    font-size: 54px; font-weight: 600; color: var(--blue);
    letter-spacing: 1px; line-height: 1;
    padding-bottom: 6px;
    border-bottom: 2px solid var(--blue-light);
  }
  .credentials { margin-top: 6px; font-size: 21px; line-height: 1.2; font-weight: 500; }
  .credentials .label { color: var(--orange-text); }
  .credentials .value { color: var(--blue); }
  .company-name {
    position: absolute; right: 60px; top: 232px;
    display: flex; align-items: center; gap: 14px;
    font-size: 40px; font-weight: 400; color: var(--white);
  }
  .company-name .mark-square { width: 22px; height: 22px; background: var(--white); }
  .contact-list {
    position: absolute; left: 60px; top: 330px;
    list-style: none; color: var(--white);
    font-size: 22px; font-weight: 500; line-height: 1.3;
  }
  .contact-list li { display: flex; align-items: flex-start; gap: 14px; }
  .contact-list svg { flex: none; width: 20px; height: 20px; margin-top: 4px; }
  .contact-list .address { margin-top: 14px; }
</style>
</head>
<body>
  <div class="business-card">
    <div class="card-face">
      <svg class="green-field" viewBox="0 0 940 510" preserveAspectRatio="none" aria-hidden="true">
        <defs>
          <linearGradient id="greenFill" x1="0" y1="0" x2="1" y2="1">
            <stop offset="0" stop-color="#93cc44"/>
            <stop offset="1" stop-color="#6fa82a"/>
          </linearGradient>
        </defs>
        <polygon points="0,295 420,200 470,225 940,120 940,510 0,510" fill="url(#greenFill)"/>
      </svg>

      <div class="identity">
        <h1 class="person-name">Owen Padick</h1>
        <p class="credentials"><span class="label">License Number</span> <span class="value">47 18 3K</span></p>
        <p class="credentials"><span class="label">ABN</span> <span class="value">53 917 648 204</span></p>
      </div>

      <div class="company-name"><span class="mark-square"></span>T &amp; R Custom Homes</div>

      <ul class="contact-list">
        <li>
          <svg viewBox="0 0 20 20"><path fill="#fff" d="M2 6c0-2 3-3 8-3s8 1 8 3v2h-4V6.5c-1-.4-2.5-.5-4-.5s-3 .1-4 .5V8H2z M4 10h12l1 7H3z"/></svg>
          02 6619 3874
        </li>
        <li>
          <svg viewBox="0 0 20 20"><rect x="5" y="1" width="10" height="18" rx="2" fill="#fff"/><rect x="7" y="4" width="6" height="8" fill="#7fb936"/></svg>
          0438 712 946
        </li>
        <li>
          <svg viewBox="0 0 20 20"><rect x="1.5" y="4.5" width="17" height="11" fill="none" stroke="#fff" stroke-width="1.6"/><path d="M2 5l8 6 8-6" fill="none" stroke="#fff" stroke-width="1.6"/></svg>
          porvina73@quellmail.com.au
        </li>
        <li class="address">
          <svg viewBox="0 0 20 20"><path fill="#fff" d="M10 2 1 10h3v8h12v-8h3z"/></svg>
          <span>Shop 3 / 17 Wendover Lane<br>Coffs Harbour, NSW 2450 Builders</span>
        </li>
      </ul>
    </div>
  </div>
</body>
</html>
```